Flyer Design Project

Design for flyer, poster and web graphic for funday. Details attached. Event is a Funday with fair ground rides, bumper cars, stalls, food, BBQ

Target Market(s)

Muslim Families with young children

Industry/Entity Type

Event

Requirements
Should not have
• No pictures of living beings or creatures. Silhouettes acceptable.

```html
<!DOCTYPE html>
<html lang="en">
<head>
<meta charset="utf-8">
<title>Family Funday</title>
<link href="https://fonts.googleapis.com/css2?family=Chewy&family=Short+Stack&display=block" rel="stylesheet">
<style>
  :root {
    --grass-dark: #2f8a1e;
    --grass-light: #6cc13a;
    --sun-yellow: #ffe600;
    --sun-orange: #f7931e;
    --deep-orange: #e8590c;
    --cream: #fff8d2;
    --white: #ffffff;
    --field-green: #1f5f12;
    --warning-red: #e3120b;
    --badge-blue: #29a3e0;
    --logo-grey: #3a3a3a;
  }
  * { margin: 0; padding: 0; box-sizing: border-box; }
  html, body { width: 846px; height: 1200px; overflow: hidden; background: #fff; }
  .flyer {
    position: relative; width: 846px; height: 1200px; overflow: hidden;
    font-family: "Short Stack", "Comic Sans MS", cursive;
  }
  .backdrop { position: absolute; inset: 0; }
  .display { font-family: "Chewy", "Comic Sans MS", cursive; font-weight: 400; }
  .abs { position: absolute; white-space: nowrap; }
  .outlined {
    color: var(--white);
    text-shadow: 3px 3px 0 var(--deep-orange), -2px -2px 0 var(--deep-orange),
                 2px -2px 0 var(--deep-orange), -2px 2px 0 var(--deep-orange),
                 0 3px 0 var(--deep-orange), 3px 0 0 var(--deep-orange);
  }

  .brand-tab {
    left: 59px; top: 0; width: 203px; height: 144px; background: var(--white);
    border-radius: 0 0 16px 16px; display: flex; align-items: center; justify-content: center;
    color: var(--logo-grey); font-size: 30px; line-height: 1.1; text-align: center;
  }
  .anniversary {
    left: 296px; top: 25px; width: 102px; height: 102px; border-radius: 50%;
    background: var(--badge-blue); color: var(--white);
    display: flex; align-items: center; justify-content: center; font-size: 46px;
  }
  .anniversary sup { font-size: 20px; margin-top: -22px; }

  .title {
    left: 112px; top: 168px; line-height: 84px; font-size: 98px; letter-spacing: 1px;
    color: var(--sun-orange);
    text-shadow: 3px 3px 0 var(--white), -3px -3px 0 var(--white), 3px -3px 0 var(--white),
                 -3px 3px 0 var(--white), 0 4px 0 var(--white), 5px 7px 0 rgba(140,60,0,.5);
  }
  .title .line2 { display: block; padding-left: 30px; }
  .tagline {
    left: 140px; top: 376px; width: 330px; text-align: center;
    font-size: 35px; line-height: 36px; color: var(--sun-yellow);
    text-shadow: 2px 2px 0 var(--deep-orange), -1px -1px 0 var(--deep-orange), 1px -1px 0 var(--deep-orange), -1px 1px 0 var(--deep-orange);
  }
  .stalls-head { left: 48px; top: 500px; font-size: 58px; }
  .stalls-list {
    left: 50px; top: 580px; list-style: none; font-size: 19px; line-height: 30px;
    color: var(--cream); text-shadow: 1px 1px 2px rgba(0,40,0,.8);
  }
  .date { left: 82px; top: 722px; font-size: 52px; line-height: 50px; }
  .date .time { display: block; padding-left: 48px; }
  .venue { left: 58px; top: 850px; font-size: 17px; line-height: 30px; color: var(--field-green); }
  .venue .place { font-size: 22px; padding-left: 190px; display: block; line-height: 34px; }
  .venue .road { padding-left: 222px; display: block; }
  .venue .dress { color: var(--warning-red); font-weight: bold; padding-left: 158px; display: block; margin-top: 12px; }
  .entry { right: 24px; top: 948px; text-align: right; color: var(--white); }
  .entry .fee { font-size: 34px; line-height: 40px; }
  .entry .note { font-size: 16px; line-height: 24px; }
  .footer {
    left: 0; width: 846px; top: 1082px; text-align: center;
    color: var(--sun-yellow); font-size: 18px; line-height: 27px;
  }
  .footer .proceeds { margin-top: 12px; color: var(--cream); }
</style>
</head>
<body>
<div class="flyer">
  <svg class="backdrop" width="846" height="1200" viewBox="0 0 846 1200">
    <defs>
      <linearGradient id="grass" x1="0" y1="0" x2="0" y2="1">
        <stop offset="0" stop-color="#3c9a25"/>
        <stop offset="1" stop-color="#6cc13a"/>
      </linearGradient>
      <linearGradient id="sunset" x1="0" y1="0" x2="0" y2="1">
        <stop offset="0" stop-color="#ffe600"/>
        <stop offset=".55" stop-color="#fbb01f"/>
        <stop offset="1" stop-color="#f07a12"/>
      </linearGradient>
      <linearGradient id="figure" x1="0" y1="0" x2="1" y2="1">
        <stop offset="0" stop-color="#fffbe0" stop-opacity=".9"/>
        <stop offset="1" stop-color="#fff3b0" stop-opacity=".6"/>
      </linearGradient>
    </defs>
    <rect width="846" height="1200" fill="url(#grass)"/>
    <path d="M0 715 C220 660 480 600 846 540 L846 1200 L0 1200 Z" fill="var(--white)"/>
    <path d="M0 748 C230 690 490 630 846 570 L846 1200 L0 1200 Z" fill="url(#sunset)"/>

    <g role="img" aria-label="Pale silhouette of a child leaping in the air">
      <path d="M420 0 L560 0 C600 80 640 150 700 220 C660 320 640 440 600 580 C560 500 520 420 480 340 C450 240 430 120 420 0 Z" fill="url(#figure)"/>
    </g>
    <g role="img" aria-label="Bunch of colourful balloons">
      <circle cx="545" cy="48" r="50" fill="#4fb0ea"/>
      <circle cx="708" cy="88" r="58" fill="#f5a62a"/>
      <circle cx="800" cy="20" r="48" fill="#f0d21e"/>
      <circle cx="628" cy="168" r="50" fill="#e52320"/>
      <circle cx="728" cy="236" r="46" fill="#d81e1a"/>
    </g>
    <g role="img" aria-label="Photographs of fairground food, ferris wheel, carousel, bumper cars and a bouncy castle">
      <circle cx="800" cy="345" r="80" fill="#c0392b"/>
      <circle cx="585" cy="518" r="90" fill="#b8521e"/>
      <circle cx="770" cy="515" r="92" fill="#3a4a2a"/>
      <circle cx="580" cy="702" r="96" fill="#b4782c"/>
      <circle cx="760" cy="712" r="90" fill="#5c6b2e"/>
      <circle cx="735" cy="872" r="80" fill="#3b1c4a"/>
    </g>
  </svg>

  <div class="abs brand-tab">sunrise<br>trust</div>
  <div class="abs anniversary display">10<sup>th</sup></div>

  <h1 class="abs title display">FAMILY<span class="line2">FUNDAY</span></h1>
  <p class="abs tagline display">A Fun Packed Day For<br>All The Family</p>

  <h2 class="abs stalls-head display outlined">Lots of Stalls</h2>
  <ul class="abs stalls-list">
    <li>BBQ and Food Stalls, Sisters-Only Area</li>
    <li>Kids Zone with Bouncy Castle, Fun Fare Rides</li>
    <li>Games &amp; Arts &amp; Crafts</li>
  </ul>

  <p class="abs date display outlined">Sunday 9th June<span class="time">11am - 7pm</span></p>
  <p class="abs venue">
    <span class="place">Maple Field</span>
    <span class="road">(off Maple Road),</span>
    Riverside Park, Eastbrook, Essex, EB1 2XY
    <span class="dress">MODEST DRESS REQUIRED</span>
  </p>

  <div class="abs entry">
    <div class="fee display outlined">Entance Fee £2</div>
    <div class="note">Free for Under 3<br>Parking £3/Vehicle</div>
  </div>

  <div class="abs footer">
    <p>For further information and stall bookings<br>email : funday@sunrisetrust.org.uk</p>
    <p class="proceeds">All proceeds from this Funday go towards the growth of Sunrise Trust.</p>
  </div>
</div>
</body>
</html>
```